Business Card design for an International Import Export House

We need a Business Card design for our import export business. We trade in Minerals, Metals, Rice, Sugar, Steel etc.. The design should be minimalistic. It may or may not contain the physical address. In case you want to include the physical address - 418 Verandah Heights, Marlow Sector 9, Halden, Westmarch, Norvia, 540117.

Target Market(s)

Steel Mills or Steel Plants, Factories, Mining businesses, Industrial houses, Government Agencies

Industry/Entity Type

Importer

Contact Information for Business Card

Business Name - Tessan Overseas

Font styles to use
Other font styles liked:
• montserrat

Requirements
Must have
• Ravi Kandola - President
• www.tessanoverseas.com
• ravi@tessanoverseas.com
• +91-987-654-3217
Nice to have
• worldwide suppliers of ores

```html
<!DOCTYPE html>
<html lang="en">
<head>
<meta charset="utf-8">
<title>Tessan Overseas – Business Card</title>
<link rel="stylesheet" href="https://fonts.googleapis.com/css2?family=Montserrat:wght@400;500;600;700&display=swap">
<style>
  :root {
    --backdrop: #e4e6e8;
    --card-light: #f7f8f9;
    --card-dark: #17191c;
    --teal: #3d8ea6;
    --ink: #1b1e21;
    --white: #ffffff;
    --muted: #d9dcdf;
  }
  * { box-sizing: border-box; margin: 0; padding: 0; }
  html, body {
    width: 1200px;
    height: 900px;
    overflow: hidden;
    background: var(--backdrop);
    font-family: "Montserrat", sans-serif;
  }
  .canvas {
    width: 1200px;
    height: 900px;
    display: flex;
    flex-direction: column;
    align-items: center;
    justify-content: center;
    gap: 44px;
  }
  .card {
    position: relative;
    width: 560px;
    height: 320px;
    box-shadow: 0 6px 18px rgba(0, 0, 0, 0.14);
  }

  /* Front */
  .card-front { background: var(--card-light); }
  .brand {
    position: absolute;
    left: 50%;
    top: 50%;
    transform: translate(-50%, -50%);
    display: flex;
    flex-direction: column;
    align-items: center;
    gap: 14px;
    white-space: nowrap;
  }
  .brand-dot {
    width: 64px;
    height: 64px;
    border-radius: 50%;
    background: var(--teal);
  }
  .brand-name {
    font-weight: 700;
    font-size: 22px;
    letter-spacing: 0.3px;
    color: var(--ink);
    text-transform: uppercase;
    white-space: nowrap;
  }
  .address-line {
    position: absolute;
    font-size: 12px;
    font-weight: 400;
    color: var(--teal);
    letter-spacing: 0.2px;
    white-space: nowrap;
  }
  .address-street { left: 28px; bottom: 24px; }
  .address-city { right: 28px; top: 24px; }

  /* Back */
  .card-back { background: var(--card-dark); }
  .holder-name {
    position: absolute;
    left: 48px;
    top: 50%;
    transform: translateY(-50%);
    font-weight: 700;
    font-size: 26px;
    color: var(--white);
    white-space: nowrap;
  }
  .contact {
    position: absolute;
    left: 320px;
    top: 104px;
    color: var(--muted);
    font-size: 13px;
    line-height: 1.55;
    white-space: nowrap;
  }
  .contact-role {
    font-size: 19px;
    font-weight: 600;
    color: var(--teal);
    margin-bottom: 2px;
  }
  .contact-phone { margin-bottom: 14px; }
  .accent { color: var(--teal); }
</style>
</head>
<body>
  <main class="canvas">
    <section class="card card-front" aria-label="Card front">
      <p class="address-line address-city">Halden, Westmarch, Norvia, 540117.</p>
      <div class="brand">
        <span class="brand-dot"></span>
        <span class="brand-name">Tessan Overseas</span>
      </div>
      <p class="address-line address-street">418 Verandah Heights, Marlow Sector 9</p>
    </section>

    <section class="card card-back" aria-label="Card back">
      <h1 class="holder-name">Ravi Kandola</h1>
      <div class="contact">
        <p class="contact-role">President</p>
        <p class="contact-phone">+91-987-654-3217</p>
        <p class="contact-email">ravi@<span class="accent">tessan</span>overseas.com</p>
        <p class="contact-web">www.tessan<span class="accent">overseas</span>.com</p>
      </div>
    </section>
  </main>
</body>
</html>
```